Banner for promote service of debit card

We are PagaVelo and we need the banners to be posted on the facebook and instagram pages.
We want something to communicate that it is an exclusive debit card full of services.
Low commissions.
Our competitors:
https://www.nortapay-pagos.it/it/home.html
https://www.zelkor-conti.it/it/
https://www.fotoreelz.it/serravanbank/
sendquillo
maybe some banner that makes the idea of a convenient debit card that everyone can use.
Girls enjoying card shopping.
Please check also website for slogans and phrases to use
https://www.pagavelo-carta.it/
Should show the services.
We must convey that it is a fast, simple card that guarantees privacy.
We need strong banners that attract people as these ban will be sponsored on instagram and facebook
Target Market(s)
People 18-35 y
Open Bank account. low commissions. Easy to use. No limits. 100% Privacy.
Requirements
Must have
- Written in Italian.

```html
<!DOCTYPE html>
<html lang="it">
<head>
<meta charset="utf-8">
<title>PagaVelo – All in One!</title>
<link rel="stylesheet" href="https://fonts.googleapis.com/css2?family=Poppins:wght@400;600;700;800&display=swap">
<style>
  :root {
    --bg-center: #eef8f9;
    --bg-edge: #d3ecef;
    --green: #4fe89c;
    --aqua: #57e6d6;
    --blue: #3b8cf2;
    --pink: #f0509a;
    --coral: #f46a6e;
    --orange: #f58a4e;
    --ink: #0c0c0c;
    --text: #1b1b1b;
    --brand-mark: #f0436f;
    --card-blue-a: #6e9cc8;
    --card-blue-b: #2f5f93;
    --card-teal-a: #4fb3a6;
    --card-teal-b: #2f8f85;
    --photo-a: #f4b27c;
    --photo-b: #d9663a;
    --photo-c: #f0c84a;
  }
  * { margin: 0; padding: 0; box-sizing: border-box; }
  html, body { width: 1200px; height: 549px; overflow: hidden; }
  body { font-family: "Poppins", sans-serif; background: #fff; }

  .banner {
    position: relative;
    width: 1200px;
    height: 549px;
    overflow: hidden;
    background: radial-gradient(ellipse at 50% 50%, var(--bg-center) 0%, var(--bg-edge) 100%);
  }
  .backdrop { position: absolute; inset: 0; width: 1200px; height: 549px; }

  .brand {
    position: absolute;
    left: 32px;
    top: 46px;
    display: flex;
    flex-direction: column;
    align-items: center;
    gap: 8px;
  }
  .brand-dot {
    width: 46px; height: 46px;
    border-radius: 50%;
    background: var(--brand-mark);
  }
  .brand-name {
    font-weight: 700;
    font-size: 21px;
    color: var(--ink);
    letter-spacing: -0.2px;
  }

  .headline {
    position: absolute;
    left: 312px;
    top: 78px;
    font-weight: 800;
    font-size: 66px;
    line-height: 1;
    color: var(--ink);
    letter-spacing: -0.5px;
  }
  .subline {
    position: absolute;
    left: 314px;
    top: 163px;
    font-weight: 800;
    font-size: 29px;
    line-height: 1;
    color: var(--ink);
    letter-spacing: -0.3px;
  }

  .features {
    position: absolute;
    left: 146px;
    top: 240px;
    list-style: none;
  }
  .features li {
    display: flex;
    align-items: center;
    height: 43px;
    font-size: 19.5px;
    color: var(--text);
  }
  .features svg { width: 16px; height: 12px; margin-right: 17px; }

  .card {
    position: absolute;
    width: 300px;
    height: 188px;
    border-radius: 14px;
    box-shadow: 0 14px 18px rgba(0,0,0,.18);
  }
  .card-back {
    left: 440px; top: 283px;
    background: linear-gradient(135deg, var(--card-teal-a), var(--card-teal-b));
    transform: rotate(12deg);
  }
  .card-front {
    left: 382px; top: 292px;
    background: radial-gradient(circle at 50% 45%, var(--card-blue-a), var(--card-blue-b));
    transform: rotate(-13deg);
  }

  .photo {
    position: absolute;
    left: 720px;
    top: 30px;
    width: 480px;
    height: 519px;
    border-radius: 48% 48% 0 0 / 30% 30% 0 0;
    background:
      linear-gradient(180deg, var(--photo-a) 0%, var(--photo-b) 45%, var(--photo-c) 100%);
    opacity: .9;
  }
</style>
</head>
<body>
<main class="banner">
  <svg class="backdrop" viewBox="0 0 1200 549" aria-hidden="true">
    <defs>
      <linearGradient id="leftWave" x1="0" y1="0" x2="0.3" y2="1">
        <stop offset="0" stop-color="var(--green)"/>
        <stop offset="0.55" stop-color="var(--aqua)"/>
        <stop offset="1" stop-color="var(--blue)"/>
      </linearGradient>
      <linearGradient id="rightWave" x1="0" y1="0" x2="0" y2="1">
        <stop offset="0" stop-color="var(--pink)"/>
        <stop offset="0.6" stop-color="var(--coral)"/>
        <stop offset="1" stop-color="var(--orange)"/>
      </linearGradient>
    </defs>
    <path class="wave-outline" fill="var(--ink)"
      d="M0 0 H282 C250 40 210 40 200 90 C190 140 250 170 215 210 C180 250 120 215 95 270 C70 320 110 350 95 400 C80 450 140 490 205 549 H0 Z"/>
    <path class="wave-left" fill="url(#leftWave)"
      d="M0 0 H268 C236 40 198 40 188 90 C178 138 236 168 202 206 C168 244 108 210 83 266 C58 318 98 350 83 400 C68 450 126 490 190 549 H0 Z"/>
    <path class="wave-outline" fill="var(--ink)"
      d="M1200 0 H1010 C1030 60 1090 80 1085 140 C1080 200 1040 250 1080 300 C1120 350 1120 420 1090 470 C1070 510 1090 530 1100 549 H1200 Z"/>
    <path class="wave-right" fill="url(#rightWave)"
      d="M1200 0 H1024 C1044 60 1104 80 1099 140 C1094 200 1054 250 1094 300 C1134 350 1134 420 1104 470 C1084 510 1104 530 1114 549 H1200 Z"/>
  </svg>

  <div class="brand">
    <span class="brand-dot"></span>
    <span class="brand-name">PagaVelo</span>
  </div>

  <h1 class="headline">All in One!</h1>
  <p class="subline">Una carta per tutti</p>

  <ul class="features">
    <li><svg viewBox="0 0 16 12"><path d="M1 6H14M9 1.5L14 6L9 10.5" fill="none" stroke="var(--ink)" stroke-width="1.8"/></svg>Enjoy your cart!</li>
    <li><svg viewBox="0 0 16 12"><path d="M1 6H14M9 1.5L14 6L9 10.5" fill="none" stroke="var(--ink)" stroke-width="1.8"/></svg>Fai quello che vuot.</li>
    <li><svg viewBox="0 0 16 12"><path d="M1 6H14M9 1.5L14 6L9 10.5" fill="none" stroke="var(--ink)" stroke-width="1.8"/></svg>Nessun limite.</li>
    <li><svg viewBox="0 0 16 12"><path d="M1 6H14M9 1.5L14 6L9 10.5" fill="none" stroke="var(--ink)" stroke-width="1.8"/></svg>Nessun controllo.</li>
  </ul>

  <div class="card card-back" role="img" aria-label="Illustrazione di una carta di debito verde acqua"></div>
  <div class="card card-front" role="img" aria-label="Illustrazione di una carta di debito blu metallizzata"></div>

  <div class="photo" role="img" aria-label="Foto di una ragazza sorridente dai capelli rossi con borse della spesa colorate"></div>
</main>
</body>
</html>
```